brolvix new business card design project

we need a new business card design. you can view info about us @ brolvix.example. i have attached an example of our previous card with our previous name that we no longer use. We really liked the design, colors etc. look below to see more info about this project. it asks for a limited number of words. please see our website for more info about our compnay.

Target Market(s)

law enforcement

Contact Information for Business Card

i have uploaded an example of what we used before that we liked.

Font styles to use
Serif

```html
<!DOCTYPE html>
<html lang="en">
<head>
<meta charset="utf-8">
<title>brolvix business card</title>
<link rel="stylesheet" href="https://fonts.googleapis.com/css2?family=Open+Sans:wght@300;400;600&display=swap">
<style>
  :root {
    --page-bg: #26282b;
    --card-top: #102340;
    --card-bottom: #0a1528;
    --ink-white: #f2f5f8;
    --ink-blue: #3a7fd0;
    --ink-muted: #c9d2dc;
  }
  * { margin: 0; padding: 0; box-sizing: border-box; }
  html, body {
    width: 1200px;
    height: 900px;
    overflow: hidden;
    background: var(--page-bg);
    font-family: "Open Sans", sans-serif;
  }
  .canvas {
    position: relative;
    width: 1200px;
    height: 900px;
  }
  .card {
    position: absolute;
    width: 540px;
    height: 310px;
    border-radius: 26px;
    background: linear-gradient(160deg, var(--card-top), var(--card-bottom));
    box-shadow: 0 18px 40px rgba(0, 0, 0, 0.45);
    color: var(--ink-white);
  }
  .card-back { left: 600px; top: 130px; }
  .card-front { left: 60px; top: 480px; }

  .wordmark {
    font-weight: 300;
    color: var(--ink-white);
    letter-spacing: 0.06em;
    white-space: nowrap;
  }
  .card-back .wordmark {
    position: absolute;
    left: 0; right: 0;
    top: 118px;
    text-align: center;
    font-size: 58px;
  }
  .card-front .wordmark {
    position: absolute;
    left: 52px;
    top: 70px;
    font-size: 40px;
  }

  .contact-block {
    position: absolute;
    left: 270px;
    top: 150px;
  }
  .person-name {
    font-size: 22px;
    font-weight: 600;
    letter-spacing: 0.02em;
    line-height: 1.1;
  }
  .job-title {
    font-size: 14px;
    font-weight: 400;
    color: var(--ink-blue);
    letter-spacing: 0.04em;
    margin-bottom: 12px;
  }
  .contact-list { list-style: none; }
  .contact-item {
    display: flex;
    align-items: center;
    gap: 9px;
    font-size: 13px;
    color: var(--ink-muted);
    line-height: 1.9;
  }
  .contact-icon {
    width: 12px;
    height: 12px;
    flex: none;
  }
</style>
</head>
<body>
<main class="canvas">

  <section class="card card-back" aria-label="Card back">
    <p class="wordmark">brolvix</p>
  </section>

  <section class="card card-front" aria-label="Card front">
    <p class="wordmark">brolvix</p>

    <div class="contact-block">
      <p class="person-name">YOUR NAME</p>
      <p class="job-title">JOB TITLE</p>
      <ul class="contact-list">
        <li class="contact-item">
          <svg class="contact-icon" viewBox="0 0 12 12" aria-hidden="true">
            <rect x="3" y="0.5" width="6" height="11" rx="1.2" fill="none" stroke="#3a7fd0" stroke-width="1.3"/>
            <circle cx="6" cy="9.3" r="0.7" fill="#3a7fd0"/>
          </svg>
          000 000 0000
        </li>
        <li class="contact-item">
          <svg class="contact-icon" viewBox="0 0 12 12" aria-hidden="true">
            <rect x="0.5" y="2" width="11" height="8" rx="1" fill="#3a7fd0"/>
            <path d="M1 2.6 L6 6.6 L11 2.6" fill="none" stroke="#0a1528" stroke-width="1"/>
          </svg>
          name@brolvix.example
        </li>
        <li class="contact-item">
          <svg class="contact-icon" viewBox="0 0 12 12" aria-hidden="true">
            <circle cx="6" cy="6" r="5.2" fill="none" stroke="#3a7fd0" stroke-width="1.1"/>
            <ellipse cx="6" cy="6" rx="2.2" ry="5.2" fill="none" stroke="#3a7fd0" stroke-width="1"/>
            <path d="M0.8 6 H11.2" stroke="#3a7fd0" stroke-width="1"/>
          </svg>
          www.brolvix.example
        </li>
      </ul>
    </div>
  </section>

</main>
</body>
</html>
```